Create Web Design Template with Source Files

I need a web design built with PSD/source files. See attached design I have made to guidance. Also I have attached an image I have used so you can use it.

I got my inspiration from this site if you would like to use it also:
http://zintaglo.com/home

PSD & html slicing and responsive designs also. So we can run across all devices.

1 page

• See attachments. Ask if you have any questions...

```html
<!DOCTYPE html>
<html lang="en">
<head>
<meta charset="utf-8">
<title>Arguvo – Debate is Life</title>
<link rel="stylesheet" href="https://fonts.googleapis.com/css2?family=Tinos:ital@0;1&family=Josefin+Sans:wght@400;600&display=swap">
<style>
:root{
  --gold:#b8924f;
  --ink:#1e1e1e;
  --text:#333;
  --muted:#777;
  --line:#e4e4e4;
  --dark:#252525;
  --paper:#fff;
}
*{margin:0;padding:0;box-sizing:border-box}
html,body{width:667px;height:1200px;overflow:hidden;background:var(--paper)}
body{position:relative;font-family:"Josefin Sans",sans-serif;color:var(--text)}
.abs{position:absolute}
.serif{font-family:"Tinos",serif}

/* header */
.site-header{left:0;top:0;width:667px;height:104px}
.social{display:flex;gap:5px}
.social span{width:10px;height:10px;border:1px solid var(--ink);border-radius:50%;display:block}
.brand{font-family:"Tinos",serif;font-size:28px;color:var(--ink);letter-spacing:1px}
.header-tools{left:506px;top:45px;display:flex;gap:4px;align-items:center}

/* hero */
.hero{left:0;top:104px;width:667px;height:174px;background:linear-gradient(100deg,#3a2c26 0%,#6b5548 30%,#4a3c34 55%,#2a2220 80%,#5a463c 100%)}
.hero-shade{position:absolute;inset:0;background:rgba(0,0,0,.35)}
.hero-title{position:absolute;left:0;width:667px;text-align:center;color:#fff;font-family:"Tinos",serif}
.hero-title.main{top:60px;font-size:26px;letter-spacing:.5px}
.hero-title.sub{top:90px;font-size:16px}

/* posts */
.post-title{font-family:"Tinos",serif;font-size:13px;color:var(--ink)}
.post-date{font-family:"Tinos",serif;font-style:italic;font-size:5px;color:var(--gold);display:flex;align-items:center;gap:6px}
.post-date::before,.post-date::after{content:"";width:16px;height:1px;background:var(--gold)}
.media{display:block}
.card-title{font-family:"Tinos",serif;font-size:7.5px;color:var(--ink)}
.card-text{font-size:4.8px;line-height:7.3px;color:var(--text)}
.btn{height:17px;display:flex;align-items:center;justify-content:center;font-size:5.5px;color:#fff;background:var(--gold)}
.btn.ghost{background:#fff;color:var(--gold);border:1px solid #ccc;font-family:"Tinos",serif;font-style:italic}
.older{font-size:5.5px;letter-spacing:.4px;color:var(--ink)}

/* sidebar */
.widget{border:1px solid var(--line);background:#fff}
.widget-label{position:absolute;left:0;width:100%;text-align:center;font-size:5.5px;letter-spacing:.5px;color:var(--ink)}
.widget.newsletter{background:var(--dark);border:none}
.widget.newsletter .widget-label{color:#fff;font-weight:600}
.cat-list{list-style:none;position:absolute;left:16px;top:24px;width:95px}
.cat-list li{font-size:5px;height:12.5px;line-height:10px;border-bottom:1px solid var(--line);color:var(--ink)}

/* footer */
.site-footer{left:0;top:1058px;width:667px;height:124px;background:var(--dark)}
.footer-bar{left:0;top:1182px;width:667px;height:18px;background:var(--dark);border-top:1px solid #5a4a30;color:#fff;font-size:4.5px;text-align:center;line-height:17px}
.footer-head{font-family:"Tinos",serif;font-size:7.5px;color:var(--gold)}
.footer-link{font-size:5.5px;color:var(--gold);letter-spacing:.3px}
.footer-date{font-size:4.5px;color:#fff}
.social.light span{border-color:#fff}
</style>
</head>
<body>

<header class="abs site-header">
  <div class="abs social" style="left:136px;top:46px"><span></span><span></span><span></span><span></span><span></span></div>
  <div class="abs brand" style="left:285px;top:32px">Arguvo</div>
  <div class="header-tools abs">
    <svg width="10" height="10" viewBox="0 0 10 10"><circle cx="4" cy="4" r="3" fill="none" stroke="#1e1e1e" stroke-width="1"/><line x1="6.2" y1="6.2" x2="9" y2="9" stroke="#1e1e1e" stroke-width="1"/></svg>
    <svg width="12" height="10" viewBox="0 0 12 10"><path d="M0 1.5h12M0 5h12M0 8.5h12" stroke="#1e1e1e" stroke-width="1"/></svg>
  </div>
</header>

<section class="abs hero" role="img" aria-label="Photo of a cheering crowd at a lively event">
  <div class="hero-shade"></div>
  <h1 class="hero-title main" style="font-weight:400">Debate is LIFE</h1>
  <p class="hero-title sub">The rest is just prep-time</p>
</section>

<!-- featured post -->
<article>
  <h2 class="abs post-title" style="left:135px;width:261px;text-align:center;top:308px;font-weight:400">Lorem is Ipsum</h2>
  <div class="abs post-date" style="left:226px;top:327px">July 22, 2017</div>
  <div class="abs media" role="img" aria-label="Photo of a long arched library hall lined with bookshelves" style="left:135px;top:338px;width:261px;height:126px;background:linear-gradient(180deg,#3a2a1e 0%,#6a4a30 45%,#2a2622 100%)"></div>
  <h3 class="abs card-title" style="left:135px;top:473px;font-weight:400">Why do we use it?</h3>
  <p class="abs card-text" style="left:135px;top:486px;width:261px">It is a long established fact that a reader will be distracted by the readable content of a page when looking at its layout. The point of using Lorem Ipsum is that it has a more-or-less normal distribution of letters, as opposed to using 'Content here, content here', making it look like readable English.</p>
  <div class="abs btn ghost" style="left:136px;top:518px;width:90px">Start Debate</div>
  <div class="abs btn" style="left:238px;top:518px;width:90px">Give Your Opinion</div>
</article>

<!-- post group one -->
<section>
  <h2 class="abs post-title" style="left:136px;top:551px;font-weight:400">Where does it from?</h2>
  <div class="abs post-date" style="left:136px;top:570px">September 19, 2017</div>

  <div class="abs media" role="img" aria-label="Black and white photo of a large explosion cloud over a palm-lined shore" style="left:135px;top:581px;width:126px;height:125px;background:linear-gradient(180deg,#5a5a5a 0%,#9a9a9a 45%,#3a3a3a 100%)"></div>
  <h3 class="abs card-title" style="left:135px;top:715px;font-weight:400">Where does it come from?</h3>
  <p class="abs card-text" style="left:135px;top:728px;width:126px">It is a long established fact that a reader will be distracted by the readable content of a page when looking at its layout.</p>
  <div class="abs btn" style="left:135px;top:761px;width:58px">Start Debate</div>
  <div class="abs btn" style="left:203px;top:761px;width:58px">Give Your Opinion</div>

  <div class="abs media" role="img" aria-label="Photo of a firefighter in gear pointing amid smoke" style="left:271px;top:581px;width:125px;height:125px;background:linear-gradient(160deg,#6a6e70 0%,#3c3a36 55%,#7a5a30 100%)"></div>
  <h3 class="abs card-title" style="left:271px;top:715px;font-weight:400">Where can I get some?</h3>
  <p class="abs card-text" style="left:271px;top:728px;width:125px">It is a long established fact that a reader will be distracted by the readable content of a page when looking at its layout.</p>
  <div class="abs btn" style="left:271px;top:761px;width:57px">Start Debate</div>
  <div class="abs btn" style="left:339px;top:761px;width:57px">Give Your Opinion</div>
</section>

<!-- post group two -->
<section>
  <h2 class="abs post-title" style="left:136px;top:793px;font-weight:400">Where does it from?</h2>
  <div class="abs post-date" style="left:136px;top:811px">September 19, 2017</div>

  <div class="abs media" role="img" aria-label="Photo of a vintage biplane in a snowy hangar" style="left:135px;top:822px;width:126px;height:125px;background:linear-gradient(180deg,#8a9aa8 0%,#b8bcc0 50%,#6a7078 100%)"></div>
  <h3 class="abs card-title" style="left:135px;top:957px;font-weight:400">Where does it come from?</h3>
  <p class="abs card-text" style="left:135px;top:970px;width:126px">It is a long established fact that a reader will be distracted by the readable content of a page when looking at its layout.</p>
  <div class="abs btn" style="left:135px;top:1002px;width:58px">Start Debate</div>
  <div class="abs btn" style="left:203px;top:1002px;width:58px">Give Your Opinion</div>

  <div class="abs media" role="img" aria-label="Photo of two men talking at a table in a dim bar" style="left:271px;top:822px;width:125px;height:125px;background:linear-gradient(180deg,#4a3e34 0%,#6a5a48 50%,#2e2822 100%)"></div>
  <h3 class="abs card-title" style="left:271px;top:957px;font-weight:400">Where can I get some?</h3>
  <p class="abs card-text" style="left:271px;top:970px;width:125px">It is a long established fact that a reader will be distracted by the readable content of a page when looking at its layout.</p>
  <div class="abs btn" style="left:271px;top:1002px;width:57px">Start Debate</div>
  <div class="abs btn" style="left:339px;top:1002px;width:57px">Give Your Opinion</div>
</section>

<div class="abs older" style="left:340px;width:56px;text-align:right;top:1036px">OLDER POSTS&gt;&gt;&gt;</div>

<!-- sidebar -->
<aside>
  <div class="abs widget" style="left:406px;top:312px;width:126px;height:125px">
    <div class="widget-label" style="top:10px">ABOUT</div>
    <div class="abs" style="left:10px;top:25px;width:104px;height:52px;background:var(--dark);display:flex;align-items:center;justify-content:center;font-family:'Tinos',serif;font-size:22px;color:#fff">Arguvo</div>
    <p class="abs card-text" style="left:10px;top:88px;width:106px;line-height:8px">Aenean commodo ligula eget dolor. Aenean massa. Cum sociis natoque penatibus.</p>
  </div>

  <div class="abs widget newsletter" style="left:406px;top:454px;width:126px;height:74px">
    <div class="widget-label" style="top:11px">SUBSCRIBE TO MY NEWSLETTER</div>
    <div class="abs" style="left:11px;top:26px;width:104px;height:14px;background:#fff;font-family:'Tinos',serif;font-style:italic;font-size:4.5px;color:#aaa;text-align:center;line-height:14px">Your Email Address</div>
    <div class="abs" style="left:11px;top:50px;width:104px;height:14px;background:#b0b0b0;font-size:5px;letter-spacing:.4px;color:var(--ink);text-align:center;line-height:15px">SUBSCRIBE</div>
  </div>

  <div class="abs widget" style="left:406px;top:546px;width:126px;height:120px">
    <div class="widget-label" style="top:10px">CATEGORIES</div>
    <ul class="cat-list">
      <li>Art</li><li>Food</li><li>Lifestyle</li><li>Movie</li><li>Music</li><li>Top</li><li>Travel</li>
    </ul>
  </div>
</aside>

<footer class="abs site-footer">
  <div class="abs" style="left:135px;top:20px;font-family:'Tinos',serif;font-size:18px;color:#fff">Arguvo</div>
  <div class="abs footer-head" style="left:135px;top:48px">Connect With Us On :</div>
  <div class="abs social light" style="left:136px;top:60px"><span></span><span></span><span></span><span></span><span></span></div>
  <div class="abs footer-head" style="left:135px;top:80px">Subscribe to Debate :</div>
  <div class="abs" style="left:135px;top:92px;width:91px;height:13px;background:#3a3a3a;font-family:'Tinos',serif;font-style:italic;font-size:4.5px;color:#888;line-height:13px;padding-left:6px">Email Address</div>
  <div class="abs" style="left:226px;top:92px;width:35px;height:13px;background:var(--gold);display:flex;align-items:center;justify-content:center">
    <svg width="8" height="7" viewBox="0 0 8 7"><path d="M0 3.5L8 0 6 7 4 4.5z" fill="#fff"/></svg>
  </div>

  <div class="abs footer-head" style="left:271px;top:29px">Recent Debates</div>
  <div class="abs footer-link" style="left:271px;top:52px">BEAUTY OF NATURE</div>
  <div class="abs footer-date" style="left:271px;top:62px">July 22, 2015</div>
  <div class="abs footer-link" style="left:271px;top:73px">FASHION MODEL SHOOT</div>
  <div class="abs footer-date" style="left:271px;top:83px">July 22, 2015</div>
  <div class="abs footer-link" style="left:271px;top:93px">GOLDEN SNOW LAND</div>
  <div class="abs footer-date" style="left:271px;top:104px">July 22, 2015</div>

  <div class="abs footer-head" style="left:406px;top:29px">Most Popular Opinions</div>
  <div class="abs footer-link" style="left:406px;top:52px">TOP 10 INGREDIENTS</div>
  <div class="abs footer-date" style="left:406px;top:62px">July 22, 2015</div>
  <div class="abs footer-link" style="left:406px;top:73px">FAMILY COMES FIRST</div>
  <div class="abs footer-date" style="left:406px;top:83px">July 22, 2015</div>
  <div class="abs footer-link" style="left:406px;top:93px">GOLDEN SNOW LAND</div>
  <div class="abs footer-date" style="left:406px;top:104px">July 22, 2015</div>
</footer>
<div class="abs footer-bar">© Copyright Arguvo 2018. All Rights Resrved, Privacy | Policy.</div>

</body>
</html>
```